Brightwater Systems Website

I am starting an IT consulting business called Brightwater Systems. I recently completed a logo contest on ArtHive and am now looking to put together a basic website. I can provide text and content but am looking for a site design with layout and graphics. I am attaching my logo below. I was thinking of a dark blue and white theme for the website (similar to the logo). However, I am open to ideas. Graphics can be a mix of business and high tech as that is the image I am trying to convey. The site will be relatively simple and probably have only 3 - 5 pages (Home, About Us, Services, Contact, etc.)
Target Market(s)
United States commercial companies and government contractors
Industry/Entity Type
Consulting
Coding
Coded - Design and coding required
Number of Pages Required
4 page
Look and feel

```html
<!DOCTYPE html>
<html lang="en">
<head>
<meta charset="utf-8">
<title>Brightwater Systems</title>
<link href="https://fonts.googleapis.com/css2?family=Raleway:wght@500;600;700;800&family=Nunito:wght@400;600&family=Open+Sans:ital@1&display=swap" rel="stylesheet">
<style>
:root{
  --navy:#0e1f45;
  --navy-deep:#0b1a3c;
  --blue:#0a7cc5;
  --ink:#232a45;
  --body:#5b6170;
  --line:#d9dde4;
  --white:#ffffff;
}
*{margin:0;padding:0;box-sizing:border-box}
html,body{width:1200px;height:2550px;overflow:hidden;background:var(--white)}
body{position:relative;font-family:'Nunito',sans-serif;color:var(--body)}
.abs{position:absolute}
.hero-bg{left:0;top:0;width:1200px;height:712px;background:linear-gradient(135deg,#1d3461 0%,#132a55 45%,#0f2149 100%)}
.hero-cut{left:0;top:540px}
.brand{font-family:'Raleway',sans-serif;font-weight:600;color:var(--white);font-size:24px;letter-spacing:2px;display:flex;align-items:center;gap:10px}
.brand-dot{width:22px;height:22px;border-radius:50%;background:var(--blue);flex:none}
.header-brand{left:60px;top:26px}
.footer-brand{left:64px;top:100px;font-size:22px;line-height:26px;width:240px}
.nav{top:35px;left:655px;display:flex;gap:24px;font-family:'Raleway',sans-serif;font-size:11px;font-weight:500;color:var(--white);letter-spacing:.3px}
.nav .active{color:var(--blue);border-bottom:2px solid var(--blue);padding-bottom:6px}
.header-phone{left:975px;top:27px;display:flex;align-items:center;gap:10px;color:var(--white);font-family:'Raleway',sans-serif;font-size:20px;font-weight:500}
.hero-title{left:62px;top:228px;font-family:'Raleway',sans-serif;font-weight:800;font-size:57px;line-height:60px;color:var(--white)}
.hero-sub{left:60px;top:352px;font-family:'Raleway',sans-serif;font-weight:600;font-size:26px;color:var(--blue)}
.hero-text{left:61px;top:390px;width:420px;font-size:13px;line-height:21px;color:var(--white)}
.btn{display:flex;align-items:center;justify-content:space-between;height:41px;padding:0 3px 0 18px;border-radius:21px;background:var(--blue);color:var(--white);font-family:'Raleway',sans-serif;font-weight:700;font-size:15px}
.btn .btn-dot{width:35px;height:35px;border-radius:50%;background:var(--white);margin-left:12px;display:flex;align-items:center;justify-content:center}
.btn .btn-dot span{width:11px;height:11px;border-radius:50%;background:var(--blue)}
.hero-btn{left:60px;top:447px;width:165px}
.eyebrow{font-family:'Raleway',sans-serif;font-size:13px;font-weight:500;color:var(--blue);letter-spacing:.3px}
.h2{font-family:'Raleway',sans-serif;font-weight:700;font-size:42px;line-height:45px;color:var(--ink)}
.h2 .accent{color:var(--blue)}
.about-eyebrow{left:180px;top:762px}
.about-title{left:180px;top:785px}
.about-copy{left:607px;top:742px;width:445px;font-size:12.5px;line-height:19.6px}
.about-copy p{margin-bottom:13px}
.about-btn{left:607px;top:1043px;width:165px}
.services{left:60px;top:1159px;width:1080px;height:510px;background:linear-gradient(120deg,#1a3160 0%,#132a55 55%,#152e5a 100%)}
.services-title{left:62px;top:74px;color:var(--white)}
.service{position:absolute;top:198px;width:280px}
.service svg{display:block;height:72px}
.service h3{margin-top:32px;font-family:'Raleway',sans-serif;font-weight:700;font-size:15px;color:var(--blue)}
.service p{margin-top:14px;font-size:12.5px;line-height:19.5px;color:#d5dbe6}
.service a{display:inline-block;margin-top:10px;font-family:'Raleway',sans-serif;font-weight:700;font-size:12px;color:var(--white);text-decoration:underline}
.contact-eyebrow{left:126px;top:1743px}
.contact-title{left:122px;top:1764px}
.contact-sub{left:126px;top:1815px;font-size:14.5px;color:var(--body)}
.form{left:561px;top:1745px;width:470px}
.field{height:42px;border:1px solid var(--line);border-radius:6px;margin-bottom:8px;padding:13px 15px;font-size:11px;color:#666;background:linear-gradient(#fff 55%,#f1f1f1)}
.field.focus{border-color:var(--blue);background:#fff;color:var(--blue)}
.field.message{height:90px;background:linear-gradient(#fff 35%,#efefef 50%)}
.submit-btn{position:absolute;left:0;top:303px;width:137px}
.banner{left:0;top:2162px;width:1200px;height:101px;background:var(--blue)}
.banner h2{position:absolute;left:61px;top:26px;font-family:'Raleway',sans-serif;font-weight:700;font-size:28px;color:var(--white)}
.banner p{position:absolute;left:62px;top:68px;font-family:'Open Sans',sans-serif;font-style:italic;font-size:15px;color:var(--white)}
.call-box{left:848px;top:2177px}
.call-text{left:933px;top:2193px;color:var(--white);font-family:'Raleway',sans-serif}
.call-text small{font-size:11px;display:block}
.call-text b{font-size:20px;font-weight:600}
.footer{left:0;top:2263px;width:1200px;height:287px;background:var(--navy-deep)}
.fcol{position:absolute;top:48px}
.fcol h4{font-family:'Raleway',sans-serif;font-weight:700;font-size:15px;color:var(--blue);margin-bottom:18px}
.sitemap li{list-style:none;color:var(--white);font-size:13px;line-height:26.5px;display:flex;align-items:center}
.sitemap li::before{content:"";width:4px;height:4px;border-radius:50%;background:var(--blue);margin-right:12px}
.crow{display:flex;gap:10px;color:var(--white);font-size:12.5px;line-height:21px;margin-bottom:14px}
.crow.big{font-size:17px}
.social{display:flex;gap:14px;margin-top:-2px}
.social span{width:38px;height:38px;border-radius:50%;background:#13264e}
.footer-rule{left:60px;top:242px;width:1080px;height:1px;background:#24355c}
.copyright{left:0;top:262px;width:1200px;text-align:center;font-size:11px;color:var(--white)}
.copyright .accent{color:var(--blue)}
</style>
</head>
<body>

<div class="abs hero-bg" role="img" aria-label="Photo of a business team collaborating in an office, tinted dark blue"></div>
<svg class="abs hero-cut" width="1200" height="180" viewBox="0 0 1200 180"><polygon points="0,172 1200,15 1200,180 0,180" fill="#fff"/></svg>

<div class="abs brand header-brand"><span class="brand-dot"></span>BRIGHTWATER SYSTEMS</div>
<nav class="abs nav"><span class="active">HOME</span><span>ABOUT US</span><span>SERVICES</span><span>CONTACT US</span></nav>
<div class="abs header-phone">
  <svg width="28" height="28" viewBox="0 0 24 24" fill="none" stroke="#0a7cc5" stroke-width="1.4"><path d="M5 3h4l2 5-2.5 1.5a11 11 0 0 0 6 6L16 13l5 2v4a2 2 0 0 1-2 2A16 16 0 0 1 3 5a2 2 0 0 1 2-2z"/><path d="M15 3a6 6 0 0 1 6 6M15 6.5a2.5 2.5 0 0 1 2.5 2.5"/></svg>
  123 456 7890
</div>

<h1 class="abs hero-title">WE PROVIDE<br>THE BEST</h1>
<div class="abs hero-sub">IT SERVICES FOR BUSINESS</div>
<p class="abs hero-text">Lorem Ipsum is simply dummy text of the printing and typesetting industry &nbsp;been the industry's standard dummy.</p>
<div class="abs btn hero-btn">LEARN MORE<span class="btn-dot"><span></span></span></div>

<div class="abs eyebrow about-eyebrow">WHO WE ARE</div>
<h2 class="abs h2 about-title">Brightwater<br><span class="accent">Systems</span></h2>
<div class="abs about-copy">
  <p>Lorem Ipsum is simply dummy text of the printing and typesetting industry. Lorem Ipsum has been the industry's standard dummy text ever since typeing industry text print.</p>
  <p>Lorem Ipsum is simply dummy text of the printing and typesetting industry. Lorem Ipsum has been the industry's standard dummy text ever since the 1500s, when an unknown printer took a galley of type and scrambled it to make a type specimen book. It has survived not only five centuries.</p>
  <p>Lorem Ipsum is simply dummy text of the printing and typesetting industry. Lorem Ipsum has been the industry's standard dummy text ever since the 1500s, when an unknown printer took a galley of type and scrambled it to make a type Lorem Ipsum is simply dummy text of the printing and typesetting industry. Lorem Ipsum has been the industry's standard dummy text ever since the 1500s, when an unknown printer.</p>
</div>
<div class="abs btn about-btn">LEARN MORE<span class="btn-dot"><span></span></span></div>

<section class="abs services" role="img" aria-label="Photo of colleagues working together at a desk, tinted dark blue">
  <h2 class="abs h2 services-title" style="color:#fff">Services We<br><span class="accent">Provide You</span></h2>
  <div class="service" style="left:64px">
    <svg width="74" height="72" viewBox="0 0 74 72" fill="none" stroke="#fff" stroke-width="2"><rect x="2" y="4" width="68" height="50" rx="2"/><path d="M2 48h68M26 64h22"/><path d="M40 38l10 10 14 6-4 10-20-4z"/></svg>
    <h3>STRATEGIC PLANNING</h3>
    <p>Lorem Ipsum has been the industry's standard dummy text ever since the, when an unknown printer took a galley of type and scrambled it to make a type specimen book.</p>
    <a>Learn More</a>
  </div>
  <div class="service" style="left:392px">
    <svg width="58" height="72" viewBox="0 0 58 72" fill="none" stroke="#fff" stroke-width="2"><circle cx="12" cy="8" r="5"/><circle cx="29" cy="8" r="5"/><circle cx="46" cy="8" r="5"/><path d="M4 22v20a25 25 0 0 0 50 0V22h-12v20a13 13 0 0 1-26 0V22z"/></svg>
    <h3>ACQUISITION SUPPORT</h3>
    <p>Lorem Ipsum has been the industry's standard dummy text ever since the, when an unknown printer took a galley of type and scrambled it to make a type specimen book.</p>
    <a>Learn More</a>
  </div>
  <div class="service" style="left:719px">
    <svg width="72" height="72" viewBox="0 0 72 72" fill="none" stroke="#fff" stroke-width="2"><rect x="4" y="22" width="64" height="44" rx="2"/><circle cx="36" cy="42" r="12"/><circle cx="36" cy="42" r="5"/><circle cx="8" cy="6" r="4"/><circle cx="36" cy="6" r="4"/><circle cx="64" cy="6" r="4"/><path d="M36 10v8M8 10v12M64 10v12"/></svg>
    <h3>PROGRAM MANAGEMENT</h3>
    <p>Lorem Ipsum has been the industry's standard dummy text ever since the, when an unknown printer took a galley of type and scrambled it to make a type specimen book.</p>
    <a>Learn More</a>
  </div>
</section>

<div class="abs eyebrow contact-eyebrow">KEEP IN TOUCH</div>
<h2 class="abs h2 contact-title">Contact <span class="accent">Us</span></h2>
<p class="abs contact-sub">If you have any Question for Contact Us Today !</p>
<form class="abs form">
  <div class="field focus">Name *</div>
  <div class="field">Email *</div>
  <div class="field">Phone *</div>
  <div class="field">Services*</div>
  <div class="field message">Message *</div>
  <div class="btn submit-btn">SUBMIT<span class="btn-dot"><span></span></span></div>
</form>

<section class="abs banner">
  <h2>Let’s Innovate</h2>
  <p>However Challenging your Transformation needs, We’re ready to Deliver the Right Solution With you.</p>
</section>
<svg class="abs call-box" width="256" height="72" viewBox="0 0 256 72"><polygon points="28,0 256,0 256,72 28,72 0,36" fill="#232a45"/><g transform="translate(42,22)" fill="none" stroke="#0a7cc5" stroke-width="1.4"><path d="M5 3h4l2 5-2.5 1.5a11 11 0 0 0 6 6L16 13l5 2v4a2 2 0 0 1-2 2A16 16 0 0 1 3 5a2 2 0 0 1 2-2z"/><path d="M15 3a6 6 0 0 1 6 6M15 6.5a2.5 2.5 0 0 1 2.5 2.5"/></g></svg>
<div class="abs call-text"><small>Call Us :</small><b>123 456 7890</b></div>

<footer class="abs footer">
  <div class="abs brand footer-brand"><span class="brand-dot"></span><span>BRIGHTWATER<br>SYSTEMS</span></div>
  <div class="fcol" style="left:337px">
    <h4>SITEMAP</h4>
    <ul class="sitemap"><li>Home</li><li>About Us</li><li>Services</li><li>Contact Us</li></ul>
  </div>
  <div class="fcol" style="left:612px">
    <h4>CONTACT US</h4>
    <div class="crow"><svg width="16" height="20" viewBox="0 0 16 20"><path d="M8 0a8 8 0 0 1 8 8c0 6-8 12-8 12S0 14 0 8a8 8 0 0 1 8-8z" fill="#0a7cc5"/><circle cx="8" cy="8" r="3" fill="#0b1a3c"/></svg><div>Brightwater Systems<br>101- lorem ipsum simple text print</div></div>
    <div class="crow big"><svg width="20" height="20" viewBox="0 0 24 24"><path d="M5 3h4l2 5-2.5 1.5a11 11 0 0 0 6 6L16 13l5 2v4a2 2 0 0 1-2 2A16 16 0 0 1 3 5a2 2 0 0 1 2-2z" fill="#0a7cc5"/></svg>123 456 7890</div>
    <div class="crow"><svg width="18" height="14" viewBox="0 0 18 14"><rect width="18" height="14" rx="1" fill="#0a7cc5"/><path d="M1 1l8 6 8-6" fill="none" stroke="#0b1a3c" stroke-width="1.5"/></svg>info@brightwatersystems.com</div>
  </div>
  <div class="fcol" style="left:887px">
    <h4>FOLLOW US</h4>
    <div class="social"><span></span><span></span><span></span></div>
  </div>
  <div class="abs footer-rule"></div>
  <div class="abs copyright">©BRIGHTWATER <span class="accent">SYSTEMS</span> – 2021 All rights reserved.</div>
</footer>

</body>
</html>
```